Brochure Template

We are looking for a new brochure template which will allow us to key in the products.

We will fill in the specification of product in the empty spaces.

Size A2 size double fold. Total of 4 pp x A3 size.

Must be in .ai file (CS3) to be given. Must provide font type as well.

One page should fit at least 20 products.
Updates

Target Market(s)

Prepare brochure template similar to the attached design.

Industry/Entity Type

Product

Requirements
Must have
• Cartvale.com.bn logo

space for product picture preferably white background.
Nice to have
• must provide font type so that we can use the design as template.

```html
<!DOCTYPE html>
<html lang="en">
<head>
<meta charset="utf-8">
<title>Product Brochure Template</title>
<link rel="stylesheet" href="https://fonts.googleapis.com/css2?family=Source+Sans+3:wght@400;600&display=swap">
<style>
  :root {
    --page-bg: #5a5a5c;
    --photo-slot: #ababae;
    --spec-text: #e2e2e2;
    --divider: #cfcfcf;
    --tag-green: #8dc63f;
    --tag-orange: #f7a23b;
    --tag-blue: #29abe2;
    --tag-text: #1e1e1e;
  }
  * { box-sizing: border-box; margin: 0; padding: 0; }
  html, body { width: 1200px; height: 850px; overflow: hidden; background: var(--page-bg); }
  .brochure-page {
    position: relative;
    width: 1200px;
    height: 850px;
    background: var(--page-bg);
    font-family: "Source Sans 3", sans-serif;
    display: grid;
    grid-template-columns: repeat(4, 292.4px);
    grid-template-rows: repeat(5, 159px);
    padding: 48px 0 0 20.4px;
  }
  .product-card { position: relative; }
  .photo-slot {
    position: absolute;
    left: 0; top: 0;
    width: 137px; height: 95px;
    background: var(--photo-slot);
    border-radius: 6px;
  }
  .card-divider {
    position: absolute;
    left: 145px; top: 0;
    height: 97px;
    border-left: 1.4px dashed var(--divider);
  }
  .spec-list {
    position: absolute;
    left: 153px; top: -1px;
    list-style: none;
    color: var(--spec-text);
    font-size: 10.6px;
    line-height: 15.6px;
    white-space: nowrap;
  }
  .product-code {
    position: absolute;
    left: 13px; top: 105px;
    width: 109px; height: 11px;
    border-radius: 5.5px;
    font-size: 6.4px;
    font-weight: 600;
    line-height: 11px;
    text-align: center;
    color: var(--tag-text);
    white-space: nowrap;
  }
  .product-code--green { background: var(--tag-green); }
  .product-code--orange { background: var(--tag-orange); }
  .product-code--blue { background: var(--tag-blue); }
</style>
</head>
<body>
<main class="brochure-page">
  <!-- Row 1 -->
  <article class="product-card"><div class="photo-slot" role="img" aria-label="Product photo area"></div><div class="card-divider"></div><ul class="spec-list"><li>Heating Power: 900 W</li><li>Storage tank water: 0.175 l</li><li>Working pressure steam:</li><li>Luminous LED. Cork</li><li>Power load: 1800 W</li><li>Power Backup: 1800 W</li></ul><p class="product-code product-code--green">PRODUCT CODE NO.: R#253/PL</p></article>
  <article class="product-card"><div class="photo-slot" role="img" aria-label="Product photo area"></div><div class="card-divider"></div><ul class="spec-list"><li>Heating Power: 900 W</li><li>Storage tank water: 0.175 l</li><li>Working pressure steam:</li><li>Luminous LED. Cork</li><li>Power load: 1800 W</li><li>Power Backup: 1800 W</li></ul><p class="product-code product-code--orange">PRODUCT CODE NO.: R#253/PL</p></article>
  <article class="product-card"><div class="photo-slot" role="img" aria-label="Product photo area"></div><div class="card-divider"></div><ul class="spec-list"><li>Heating Power: 900 W</li><li>Storage tank water: 0.175 l</li><li>Working pressure steam:</li><li>Luminous LED. Cork</li><li>Power load: 1800 W</li><li>Power Backup: 1800 W</li></ul><p class="product-code product-code--green">PRODUCT CODE NO.: R#253/PL</p></article>
  <article class="product-card"><div class="photo-slot" role="img" aria-label="Product photo area"></div><div class="card-divider"></div><ul class="spec-list"><li>Heating Power: 900 W</li><li>Storage tank water: 0.175 l</li><li>Working pressure steam:</li><li>Luminous LED. Cork</li><li>Power load: 1800 W</li><li>Power Backup: 1800 W</li></ul><p class="product-code product-code--blue">PRODUCT CODE NO.: R#253/PL</p></article>
  <!-- Row 2 -->
  <article class="product-card"><div class="photo-slot" role="img" aria-label="Product photo area"></div><div class="card-divider"></div><ul class="spec-list"><li>Heating Power: 900 W</li><li>Storage tank water: 0.175 l</li><li>Working pressure steam:</li><li>Luminous LED. Cork</li><li>Power load: 1800 W</li><li>Power Backup: 1800 W</li></ul><p class="product-code product-code--green">PRODUCT CODE NO.: R#253/PL</p></article>
  <article class="product-card"><div class="photo-slot" role="img" aria-label="Product photo area"></div><div class="card-divider"></div><ul class="spec-list"><li>Heating Power: 900 W</li><li>Storage tank water: 0.175 l</li><li>Working pressure steam:</li><li>Luminous LED. Cork</li><li>Power load: 1800 W</li><li>Power Backup: 1800 W</li></ul><p class="product-code product-code--orange">PRODUCT CODE NO.: R#253/PL</p></article>
  <article class="product-card"><div class="photo-slot" role="img" aria-label="Product photo area"></div><div class="card-divider"></div><ul class="spec-list"><li>Heating Power: 900 W</li><li>Storage tank water: 0.175 l</li><li>Working pressure steam:</li><li>Luminous LED. Cork</li><li>Power load: 1800 W</li><li>Power Backup: 1800 W</li></ul><p class="product-code product-code--green">PRODUCT CODE NO.: R#253/PL</p></article>
  <article class="product-card"><div class="photo-slot" role="img" aria-label="Product photo area"></div><div class="card-divider"></div><ul class="spec-list"><li>Heating Power: 900 W</li><li>Storage tank water: 0.175 l</li><li>Working pressure steam:</li><li>Luminous LED. Cork</li><li>Power load: 1800 W</li><li>Power Backup: 1800 W</li></ul><p class="product-code product-code--blue">PRODUCT CODE NO.: R#253/PL</p></article>
  <!-- Row 3 -->
  <article class="product-card"><div class="photo-slot" role="img" aria-label="Product photo area"></div><div class="card-divider"></div><ul class="spec-list"><li>Heating Power: 900 W</li><li>Storage tank water: 0.175 l</li><li>Working pressure steam:</li><li>Luminous LED. Cork</li><li>Power load: 1800 W</li><li>Power Backup: 1800 W</li></ul><p class="product-code product-code--green">PRODUCT CODE NO.: R#253/PL</p></article>
  <article class="product-card"><div class="photo-slot" role="img" aria-label="Product photo area"></div><div class="card-divider"></div><ul class="spec-list"><li>Heating Power: 900 W</li><li>Storage tank water: 0.175 l</li><li>Working pressure steam:</li><li>Luminous LED. Cork</li><li>Power load: 1800 W</li><li>Power Backup: 1800 W</li></ul><p class="product-code product-code--orange">PRODUCT CODE NO.: R#253/PL</p></article>
  <article class="product-card"><div class="photo-slot" role="img" aria-label="Product photo area"></div><div class="card-divider"></div><ul class="spec-list"><li>Heating Power: 900 W</li><li>Storage tank water: 0.175 l</li><li>Working pressure steam:</li><li>Luminous LED. Cork</li><li>Power load: 1800 W</li><li>Power Backup: 1800 W</li></ul><p class="product-code product-code--green">PRODUCT CODE NO.: R#253/PL</p></article>
  <article class="product-card"><div class="photo-slot" role="img" aria-label="Product photo area"></div><div class="card-divider"></div><ul class="spec-list"><li>Heating Power: 900 W</li><li>Storage tank water: 0.175 l</li><li>Working pressure steam:</li><li>Luminous LED. Cork</li><li>Power load: 1800 W</li><li>Power Backup: 1800 W</li></ul><p class="product-code product-code--blue">PRODUCT CODE NO.: R#253/PL</p></article>
  <!-- Row 4 -->
  <article class="product-card"><div class="photo-slot" role="img" aria-label="Product photo area"></div><div class="card-divider"></div><ul class="spec-list"><li>Heating Power: 900 W</li><li>Storage tank water: 0.175 l</li><li>Working pressure steam:</li><li>Luminous LED. Cork</li><li>Power load: 1800 W</li><li>Power Backup: 1800 W</li></ul><p class="product-code product-code--green">PRODUCT CODE NO.: R#253/PL</p></article>
  <article class="product-card"><div class="photo-slot" role="img" aria-label="Product photo area"></div><div class="card-divider"></div><ul class="spec-list"><li>Heating Power: 900 W</li><li>Storage tank water: 0.175 l</li><li>Working pressure steam:</li><li>Luminous LED. Cork</li><li>Power load: 1800 W</li><li>Power Backup: 1800 W</li></ul><p class="product-code product-code--orange">PRODUCT CODE NO.: R#253/PL</p></article>
  <article class="product-card"><div class="photo-slot" role="img" aria-label="Product photo area"></div><div class="card-divider"></div><ul class="spec-list"><li>Heating Power: 900 W</li><li>Storage tank water: 0.175 l</li><li>Working pressure steam:</li><li>Luminous LED. Cork</li><li>Power load: 1800 W</li><li>Power Backup: 1800 W</li></ul><p class="product-code product-code--green">PRODUCT CODE NO.: R#253/PL</p></article>
  <article class="product-card"><div class="photo-slot" role="img" aria-label="Product photo area"></div><div class="card-divider"></div><ul class="spec-list"><li>Heating Power: 900 W</li><li>Storage tank water: 0.175 l</li><li>Working pressure steam:</li><li>Luminous LED. Cork</li><li>Power load: 1800 W</li><li>Power Backup: 1800 W</li></ul><p class="product-code product-code--blue">PRODUCT CODE NO.: R#253/PL</p></article>
  <!-- Row 5 -->
  <article class="product-card"><div class="photo-slot" role="img" aria-label="Product photo area"></div><div class="card-divider"></div><ul class="spec-list"><li>Heating Power: 900 W</li><li>Storage tank water: 0.175 l</li><li>Working pressure steam:</li><li>Luminous LED. Cork</li><li>Power load: 1800 W</li><li>Power Backup: 1800 W</li></ul><p class="product-code product-code--green">PRODUCT CODE NO.: R#253/PL</p></article>
  <article class="product-card"><div class="photo-slot" role="img" aria-label="Product photo area"></div><div class="card-divider"></div><ul class="spec-list"><li>Heating Power: 900 W</li><li>Storage tank water: 0.175 l</li><li>Working pressure steam:</li><li>Luminous LED. Cork</li><li>Power load: 1800 W</li><li>Power Backup: 1800 W</li></ul><p class="product-code product-code--orange">PRODUCT CODE NO.: R#253/PL</p></article>
  <article class="product-card"><div class="photo-slot" role="img" aria-label="Product photo area"></div><div class="card-divider"></div><ul class="spec-list"><li>Heating Power: 900 W</li><li>Storage tank water: 0.175 l</li><li>Working pressure steam:</li><li>Luminous LED. Cork</li><li>Power load: 1800 W</li><li>Power Backup: 1800 W</li></ul><p class="product-code product-code--green">PRODUCT CODE NO.: R#253/PL</p></article>
  <article class="product-card"><div class="photo-slot" role="img" aria-label="Product photo area"></div><div class="card-divider"></div><ul class="spec-list"><li>Heating Power: 900 W</li><li>Storage tank water: 0.175 l</li><li>Working pressure steam:</li><li>Luminous LED. Cork</li><li>Power load: 1800 W</li><li>Power Backup: 1800 W</li></ul><p class="product-code product-code--blue">PRODUCT CODE NO.: R#253/PL</p></article>
</main>
</body>
</html>
```